Homepage design for Dutch Job Posting Site (Varo-Plek.nl)

We need a redesign of our homepage www.Varo-Plek.nl to make it very clear what we do. We are an online job posting portal and are looking to recruit clients and professionals on a single page.

The Homepage will focus on CLIENTS (OPDRACHTGEVERS), with the idea that if we have a lot of jobs posted, then the professionals will come.

Important to know is that we now have ONE REGISTRATION for both professionals and clients - so there is no need for two separate registration options.

Also important to know is that the JOB POSTER pages will have a GREEN hyperlinks color (see the color above the OPDRACHTGEVER at the top of the screen) and the Professionals will have a BLUE hyperlinks color (see the color above the PROFESSIONAL at the top of the screen).

At the top of the page, we would like a 4 page slider (we will do the coding but just want 4 slides) that shows how it works and what makes us unique. In the examples below, you can see that we have already done 2 of them, and we will ask the designer to help do the other two once the project is awarded.

You can see from the images provided that we have already done most of the work. The HEADER WRAP and the FOOTER are already done, and you can use these in your examples.

Notice also in the image "Homepage-BannerBlank" the image used in the center. It is an image that is only as wide as the header and then fades off into a background image that we can use repeat-x in the css of the site which fills the screen on any monitor resolution. If you don't understand what I just wrote, you probably are not the right designer for the job.

Notice also that the two images "NU AANMELDEN" and "VARO-PLEK ESCROW" use background images that have a SUBTLE background image - it is not just a gradient color change. This is what we LOVE in the design so far.

You can see that our design is already very far advanced, so what we are looking for in a new design are not the overall redesign, but specific, subtle design improvements to give the page a CLEAN, FRESH, MODERN look without being busy and crowded.

Where we specifically want help is in these areas. The designers that show us these elements will be the ones selected. All others will be eliminated without further comment:
a) How to blend in the Varo-Plek logo into the header design without taking up more HEIGHT (we have done a white overlay, but this is where you can prove to us that you are great.

b) We need a font for our h1 tags in our site. This will be the same font used in "Laatste Opdrachten" "Laatste Blogs" "Zoek uw professional per categorie of rubriek". Do not use a webfont (Arial or Verdana). Instead, refer to the examples provided for inspiration of a font that best suits the site for a header.

c) We need better containers for "Laatse opdrachten", "Laatste Blogs" and Zoek uw professional per categorie of rubriek. They can have colors or just borders or just outlines. They should compliment the site look though and not distract from it.

d) Transitions between the containers and other elements. Right now they are all just boxy and separate, but there could be some overlap, some shadows, an image divider (as there is between "Laatste Blogs" and TarnoRadio) but again, the transitions need top complement the design and not take it over.

Sites that appeal to us for what we are looking for are:
- brisket.com
- www.lumivault.com*
- Tallyforge.com*
- Quendalux.com*
*What we like here are both the top PROMINENT central message and then the smaller subtler design transitions underneath.

Feel free to use images or icons to complement the look, but it must be clean, fresh and modern.

Target Market(s)

University-educated Job Posters between 18 - 45

Industry/Entity Type

Online

Requirements
Must have
• - The header wrapper height but be exactly as it is on the images given. This header will be used on all the inner pages and therefore cannot be any higher than what is shown.
- Focus on the 4 tasks outlined
- Keep it clean! We love white, but also like small icons where appropriate and clean transitions.
Nice to have
• Dutch text is NOT important, we can translate.
Should not have
• No cluttered design.

```html
<!DOCTYPE html>
<html lang="nl">
<head>
<meta charset="utf-8">
<title>Varo-Plek – Samen aan de slag</title>
<link rel="stylesheet" href="https://fonts.googleapis.com/css2?family=Questrial&family=Arimo:ital,wght@0,400;0,700;1,400;1,700&family=Carlito:wght@400;700&display=swap">
<style>
:root{
  --green:#6aa51c;
  --green-light:#8cc83a;
  --green-dark:#4f8a0f;
  --ink:#2f2f2f;
  --text:#444;
  --muted:#777;
  --band:#d6d6d6;
  --card:#d2d2d2;
  --footer:#c4c4c4;
  --bar:#2b2b2b;
  --white:#fff;
  --radio:#c8161d;
}
*{box-sizing:border-box;margin:0;padding:0}
html,body{width:900px;height:1200px;overflow:hidden}
body{position:relative;font-family:"Arimo",Arial,sans-serif;color:var(--text);
  background:linear-gradient(#fbfbfb 0,#f3f3f3 420px,#d9d9d9 420px,#e2e2e2 1000px);}
a{color:inherit;text-decoration:none}
.abs{position:absolute}

/* header */
.header{position:absolute;left:0;top:0;width:900px;height:100px;
  background:linear-gradient(#fff,#f4f4f4);border-bottom:1px solid #e6e6e6}
.brand{position:absolute;left:93px;top:-4px;width:274px;height:104px;background:var(--white);
  transform:skewX(-4deg);box-shadow:0 3px 8px rgba(0,0,0,.25);border:1px solid #ddd}
.brand-name{position:absolute;left:120px;top:22px;display:flex;align-items:center;gap:12px;
  font-family:"Questrial",sans-serif;font-size:44px;color:var(--ink)}
.brand-dot{width:22px;height:22px;border-radius:50%;background:var(--green)}
.audience{position:absolute;left:428px;top:22px;font-size:11.5px;display:flex;gap:14px}
.audience .on{color:var(--ink);border-bottom:2px solid var(--green);padding-bottom:3px}
.audience .off{color:#555}
.topline{position:absolute;left:420px;top:43px;width:380px;height:1px;background:#ddd}
.account{position:absolute;left:677px;top:22px;font-size:12px;color:var(--ink)}
.nav{position:absolute;top:67px;left:389px;font-size:12px;color:var(--green)}
.nav a{position:absolute;top:0;height:21px;line-height:21px;white-space:nowrap}
.nav .active{background:var(--green);color:#fff;padding:0 12px;border-radius:2px;left:0}

/* hero */
.headline{position:absolute;top:150px;left:0;width:900px;text-align:center;
  font-family:"Questrial",sans-serif;font-size:24px;color:#333;letter-spacing:.3px}
.art{position:absolute;border-radius:6px}
.slider-dots{position:absolute;left:107px;top:388px;display:flex;gap:4px}
.slider-dots span{width:13px;height:13px;border-radius:50%;background:#cfcfcf;border:1px solid #bbb}
.slider-dots span:first-child{background:#aaa}
.demo{position:absolute;left:303px;top:367px;width:300px;height:44px;border-radius:3px;
  background:linear-gradient(#9ed24d,#5c9d15);color:#fff;font-family:"Questrial",sans-serif;
  font-size:22px;line-height:44px;padding-left:18px;box-shadow:0 2px 3px rgba(0,0,0,.3)}
.demo .go{position:absolute;right:14px;top:11px;width:22px;height:22px;border-radius:50%;background:#3d6f0c}

/* search */
.search{position:absolute;left:91px;top:420px;width:718px;height:147px;background:var(--white);
  box-shadow:0 3px 6px rgba(0,0,0,.25)}
.search-divider{position:absolute;left:362px;top:14px;width:1px;height:82px;background:#ccc}
.search h2{position:absolute;font-family:"Arimo",sans-serif;font-style:italic;font-weight:400;
  color:var(--green);font-size:18px}
.field{position:absolute;height:20px;border:1px solid #bbb;background:#fff;font-size:9px;
  line-height:18px;padding-left:5px;color:#333;border-radius:2px;white-space:nowrap}
.field.select::after{content:"";position:absolute;right:2px;top:2px;width:13px;height:14px;
  background:#eee;border:1px solid #999}
.hint{position:absolute;font-size:7px;color:#555;white-space:nowrap}
.btn{position:absolute;background:linear-gradient(#8cc83a,#5f9b15);color:#fff;font-weight:700;
  font-size:11px;text-align:center;border-radius:2px;white-space:nowrap}
.search .note{position:absolute;font-style:italic;font-size:9px;color:#666;white-space:nowrap}
.radio-badge{position:absolute;left:625px;top:116px;display:flex;align-items:center;gap:5px;
  font-size:12px;font-weight:700;color:var(--radio);white-space:nowrap}
.radio-badge i{width:12px;height:12px;background:var(--radio)}

/* cards */
.card{position:absolute;top:587px;width:219px;height:226px;background:var(--card);
  border:1px solid #bdbdbd;box-shadow:0 1px 3px rgba(0,0,0,.2)}
.card h3{font-size:14px;color:var(--green-dark);font-weight:700;text-align:center;margin-top:8px}
.card .lead{position:absolute;left:18px;top:35px;width:184px;height:78px;background:#fff;
  border:2px solid var(--green);display:flex;gap:6px;padding:6px}
.card .lead .pic{width:66px;height:60px;border-radius:4px;flex:none}
.card .lead p{font-style:italic;font-weight:700;font-size:10px;line-height:13px;color:#444}
.card ul{position:absolute;left:8px;top:131px;list-style:none;font-size:9.5px;color:#333}
.card li{height:16px;line-height:16px;white-space:nowrap}
.card li::before{content:"→";color:var(--green);font-weight:700;margin-right:6px}
.card .btn{left:64px;top:188px;width:136px;height:22px;line-height:22px;font-size:12px}

/* latest jobs */
.latest{position:absolute;left:583px;top:593px;width:221px}
.latest h2{font-size:14px;font-weight:700;color:var(--green-dark);padding-bottom:6px;border-bottom:1px solid #bbb}
.job{height:129px;border-bottom:1px solid #bbb;padding-top:7px;overflow:hidden}
.job h4{font-style:italic;font-weight:700;font-size:11px;line-height:13px;color:#777;white-space:nowrap}
.job .cat{font-style:italic;font-weight:700;font-size:10px;line-height:12px;color:var(--green);margin:2px 0 4px}
.job p{font-size:9px;line-height:11.5px;height:69px;overflow:hidden;color:#333}
.job .meta{display:flex;justify-content:space-between;font-size:9px;line-height:12px;margin-top:6px;white-space:nowrap}
.job .meta span:first-child{color:var(--green)}
.job .meta span:last-child{font-style:italic;color:#777}

/* welcome */
.welcome{position:absolute;left:97px;top:836px;width:448px}
.welcome h1{font-family:"Arimo",sans-serif;font-size:17px;color:#222;font-weight:700;margin-bottom:7px}
.welcome h1 span{color:var(--green)}
.welcome p{font-family:"Carlito",sans-serif;font-size:10.5px;line-height:12.8px;color:#222;margin-bottom:12px}

/* footer */
.footer{position:absolute;left:0;top:1005px;width:900px;height:158px;
  background:linear-gradient(#b8b8b8,#d2d2d2);border-top:3px solid var(--green)}
.footer-brand{position:absolute;left:107px;top:18px;display:flex;align-items:center;gap:8px;
  font-family:"Questrial",sans-serif;font-size:30px;color:#9a9a9a}
.footer-brand i{width:14px;height:14px;border-radius:50%;background:#a8a8a8}
.fcol{position:absolute;top:22px}
.fcol h5{font-style:italic;font-weight:700;font-size:10.5px;color:var(--green-dark);margin-bottom:9px}
.fcol li{list-style:none;font-size:9px;line-height:12.8px;color:#222;white-space:nowrap}
.fcol li.all{font-weight:700;font-style:italic}
.bar{position:absolute;left:0;top:1163px;width:900px;height:37px;background:var(--bar);color:#fff;
  font-size:9px;font-weight:700}
.bar .copy{position:absolute;left:100px;top:14px}
.bar .follow{position:absolute;left:684px;top:14px;display:flex;gap:4px;align-items:center}
.bar .follow i{width:11px;height:11px;border-radius:2px;display:inline-block}
</style>
</head>
<body>

<header class="header">
  <div class="brand"></div>
  <div class="brand-name"><span class="brand-dot"></span>Varo-Plek</div>
  <div class="audience"><a class="on" href="#">Opdrachtgever</a><a class="off" href="#">Professional</a></div>
  <div class="account">Aanmelden | Inloggen</div>
  <div class="topline"></div>
  <nav class="nav">
    <a class="active" href="#">Home</a>
    <a href="#" style="left:74px">Opdrachten</a>
    <a href="#" style="left:172px">Mijn Kantoor</a>
    <a href="#" style="left:271px">Hoe het werkt</a>
    <a href="#" style="left:378px">Blog</a>
  </nav>
</header>

<section class="hero">
  <h1 class="headline">GET WORLD CLASS WERKT. ONLINE. 100% VEILIG EN RISICO-FREE</h1>
  <div class="art" role="img" aria-label="Kaart van Nederland in donkergrijs" style="left:193px;top:195px;width:94px;height:170px;background:linear-gradient(#777,#444)"></div>
  <svg class="abs" style="left:312px;top:238px" width="44" height="20" viewBox="0 0 44 20"><path d="M2 14 Q22 0 40 10" fill="none" stroke="#999" stroke-width="2"/><path d="M34 5 L41 10 L33 13" fill="none" stroke="#999" stroke-width="2"/></svg>
  <div class="art" role="img" aria-label="Figuur met veilinghamer op een sokkel" style="left:367px;top:193px;width:140px;height:172px;background:radial-gradient(circle at 50% 45%,#f2f2f2,#bdbdbd 70%,#f6f6f6 100%)"></div>
  <svg class="abs" style="left:540px;top:238px" width="44" height="20" viewBox="0 0 44 20"><path d="M2 14 Q22 0 40 10" fill="none" stroke="#999" stroke-width="2"/><path d="M34 5 L41 10 L33 13" fill="none" stroke="#999" stroke-width="2"/></svg>
  <div class="art" role="img" aria-label="Twee hangende bordjes met keurmerken" style="left:600px;top:238px;width:107px;height:62px;background:linear-gradient(#6a6a6a,#3e3e3e)"></div>
  <div class="slider-dots"><span></span><span></span><span></span><span></span></div>
  <a class="demo" href="#">Klik for a demo or tour<span class="go"><svg width="22" height="22" viewBox="0 0 22 22"><path d="M9 6 L14 11 L9 16" fill="none" stroke="#fff" stroke-width="2.5"/></svg></span></a>
</section>

<section class="search">
  <h2 style="left:49px;top:11px">Zoek Professionals</h2>
  <div class="field" style="left:21px;top:36px;width:161px">Vul hier uw zoekopdracht in</div>
  <div class="field select" style="left:188px;top:36px;width:161px">Alle categorieën</div>
  <div class="hint" style="left:21px;top:61px">De juiste Professional vinden voor uw opdracht</div>
  <div class="btn" style="left:21px;top:72px;width:77px;height:20px;line-height:20px">Zoeken</div>

  <div class="search-divider"></div>

  <h2 style="left:402px;top:11px">Zoek Opdrachten</h2>
  <div class="field" style="left:374px;top:36px;width:162px">Vul hier uw zoekopdracht in</div>
  <div class="field select" style="left:542px;top:36px;width:159px">Alle categorieën</div>
  <div class="hint" style="left:374px;top:61px">Verdien geld door de juiste Opdracht te vinden</div>
  <div class="btn" style="left:374px;top:72px;width:78px;height:20px;line-height:20px">Zoeken</div>

  <div class="note" style="left:18px;top:121px">Wilt u meer Advance Search?</div>
  <div class="btn" style="left:162px;top:116px;width:143px;height:20px;line-height:20px;font-size:9px">Klik hier voor Advance zoeken</div>
  <div class="note" style="left:356px;top:121px">Zoals gehoord op TarnoRadio! Beluister direct onze radiospot</div>
  <div class="radio-badge"><i></i>TarnoRadio</div>
</section>

<article class="card" style="left:97px">
  <h3>Aanmelden als Opdrachtgever</h3>
  <div class="lead"><div class="pic" role="img" aria-label="Twee figuren die elkaar de hand schudden" style="background:linear-gradient(#eee,#bbb)"></div>
    <p>Schrijf u nu in bij Varo-Plek, plaats geheel gratis uw opdrachten en</p></div>
  <ul><li>Stop de zoektocht naar de juiste professional</li><li>Laat professionals vechten om uw opdracht</li><li>Betaal op een veilige wijze</li></ul>
  <a class="btn" href="#">Read More</a>
</article>

<article class="card" style="left:331px">
  <h3>Aanmelden als Professional</h3>
  <div class="lead"><div class="pic" role="img" aria-label="Twee figuren met puzzelstukken" style="background:linear-gradient(#f0e0c8,#d4b080)"></div>
    <p>Schrijf u nu geheel gratis in bij Varo-Plek, kies het juiste abonnement en</p></div>
  <ul><li>Vind eenvoudig nieuwe opdrachten</li><li>Creëer uw online portfolio voor klanten</li><li>Regel al uw zaken via uw Virtuele Kantoor</li></ul>
  <a class="btn" href="#">Read More</a>
</article>

<aside class="latest">
  <h2>Laatste Opdrachten</h2>
  <div class="job"><h4>VOIP telefonie in kantoor instellen</h4><div class="cat">IT</div>
    <p>Voor mijn kantoor tot 5 werkplekken ben ik op zoek naar een bedrijf dat de telefonie voor mij op de juiste wijze kan instellen. Ik heb een Belvox online nummer, wat het vaste telefoonnummer moet worden, waarop alle medewerkers te bereiken zijn. Verder moet er doorverbonden kunnen worden naar specifi...</p>
    <div class="meta"><span>7 dagen geleden</span><span>Opdracht bekijken &gt;</span></div></div>
  <div class="job"><h4>VOIP telefonie in kantoor instellen</h4><div class="cat">IT</div>
    <p>Voor mijn kantoor tot 5 werkplekken ben ik op zoek naar een bedrijf dat de telefonie voor mij op de juiste wijze kan instellen. Ik heb een Belvox online nummer, wat het vaste telefoonnummer moet worden, waarop alle medewerkers te bereiken zijn. Verder moet er doorverbonden kunnen worden naar specifi...</p>
    <div class="meta"><span>7 dagen geleden</span><span>Opdracht bekijken &gt;</span></div></div>
  <div class="job" style="border-bottom:0"><h4>VOIP telefonie in kantoor instellen</h4><div class="cat">IT</div>
    <p>Voor mijn kantoor tot 5 werkplekken ben ik op zoek naar een bedrijf dat de telefonie voor mij op de juiste wijze kan instellen. Ik heb een Belvox online nummer, wat het vaste telefoonnummer moet worden, waarop alle medewerkers te bereiken zijn. Verder moet er doorverbonden kunnen worden naar specifi...</p>
    <div class="meta"><span>7 dagen geleden</span><span>Opdracht bekijken &gt;</span></div></div>
</aside>

<section class="welcome">
  <h1>Welcome to <span>Varo-Plek</span></h1>
  <p>Lorem Ipsum is simply dummy text of the printing and typesetting industry. Lorem Ipsum has been the industry's standard dummy text ever since the 1500s, when an unknown printer took a galley of type and scrambled it to make a type specimen book. It has survived not only five centuries, but also the leap into electronic typesetting, remaining essentially unchanged. It was popularised in the 1960s with the release of Kernwell sheets containing Lorem Ipsum passages, and more recently with desktop publishing software like Pressling Layout including versions of Lorem Ipsum.</p>
  <p>Lorem Ipsum is simply dummy text of the printing and typesetting industry. Lorem Ipsum has been the industry's standard dummy text ever since the 1500s, when an unknown printer took a galley of type and scrambled it to make a type specimen book. It has survived not only five centuries, but also the leap into .</p>
</section>

<footer class="footer">
  <div class="footer-brand"><i></i>Varo-Plek</div>
  <div class="fcol" style="left:280px"><h5>Zoek opdrachten per categorie</h5><ul>
    <li>Advies &amp; Educatie</li><li>Design &amp; Multimedia</li><li>Dieren</li><li>Engineering / Manufacturing</li><li>Evenementen en Vrije tijd</li><li>Financiëel &amp; Administratief</li><li>Gezondheid, Welzijn en Mens</li><li class="all">Bekijk alles</li></ul></div>
  <div class="fcol" style="left:452px"><h5>Opdrachtgevers</h5><ul><li>Plaats uw opdracht</li><li>Zoek professionals</li><li>Mijn Kantoor</li></ul></div>
  <div class="fcol" style="left:577px"><h5>Professionals</h5><ul><li>Zoek opdrachten</li><li>Mijn Kantoor</li></ul></div>
  <div class="fcol" style="left:688px"><h5>Bedrijf</h5><ul><li>Over Varo-Plek</li><li>Hoe het werkt</li><li>FAQ</li><li>Contact</li><li>Privacy beleid</li><li>Financiëel &amp; Administratief</li><li>Geschillenregeling</li></ul></div>
</footer>
<div class="bar">
  <div class="copy">© 2011 Varo-Plek.nl . All Rights Reserved</div>
  <div class="follow">Volg ons op:&nbsp;<i style="background:#3b5998"></i><i style="background:#3aa9e0"></i><i style="background:#2a6ea8"></i><i style="background:#e8892b"></i></div>
</div>

</body>
</html>
```